AMBER HARBOUR WEB

We need a home design in wordpress, we have now a web but we would like to improve it. Our current web is www.amberharbourvillas.example Our business is holliday rental of villas in Ibiza. Our guest must know that we are a reliable company, professional and with experience and good reviews. We want them to click in our reservation engine: https://bookings.amberharbourvillas.example/en/ and make reservation in our website. We would also like to say that all the properties that we have are just us who commercialize so we have best price available. Many people are going to see our villas in staylodgr.example and look to our website to make a reservation with us so we need to show them that they are at the right place and click at our link to our reservation engine. What make us special is that we are a local company, we are from Ibiza, Our guests are always received in person by the Amber Harbour Villas team. You will enjoy extensive tourist information when you check in and during the entire stay. You will be attended by ChatPelt and calls, always happy to help so that you have a happy and fun stay! Our guest stay is better than in hotel as they have more spece, private swiming pool, private garden, barbeque ... To rent a villa is the best way to stay in Ibiza. We also have a promotional video: https://vidshare.example/Qm7pTz3RxLa Let our philosophy be shown, we think that coming on holiday to Ibiza implies seeing the nature that we have in Ibiza, hence our name AMBER HARBOUR, like the pins that almost touch the sea in Ibiza, or the posidonea meadows where the intense green of the seaweed and the blue of the sea. We are aware of the environment, and we love Ibiza. For us, the client who visits Ibiza, should rent a car, go around the island, eat in a restaurant one day in front of the sea, is a night of partying to the discs, go shopping, visit the ancient heritage of Umanity, make some aquatic sport, enjoy the pool, those are for us Ibiza.

Target Market(s)

Europe, people from Holand, UK, Germany, France, Spain ...

Industry/Entity Type

Tourism

Colors

Designer to choose colors to be used in the design.

Requirements
Must have
• Pictures of Ibiza.
Nice to have
• Our name Amber Harbour Villas is beacuse in Ibiza there is forest that almost touch the watter of the Mediterranean sea, so you can see green of the forest and blue of the sea and the sky. And also beacause under the watter of the sea there is a plant called Posidonia that is also green please see the picture of posidonia.

```html
<!DOCTYPE html>
<html lang="en">
<head>
<meta charset="utf-8">
<title>Amber Harbour Villas – Home</title>
<link href="https://fonts.googleapis.com/css2?family=Old+Standard+TT:wght@400;700&family=Montserrat:wght@400;500;600;700&family=Open+Sans:wght@400;600&display=swap" rel="stylesheet">
<style>
:root{
  --blue:#2b9ad3;
  --blue-light:#35b0e3;
  --green:#587d33;
  --green-dark:#4a6d2a;
  --lime:#9dbb34;
  --page:#f4f4f4;
  --ink:#333;
  --muted:#666;
  --white:#fff;
  --grad:linear-gradient(90deg,var(--green) 0%,var(--blue-light) 100%);
}
*{box-sizing:border-box;margin:0;padding:0}
html,body{width:1200px;height:3377px;overflow:hidden}
body{background:var(--page);font-family:"Open Sans",sans-serif;color:var(--ink);position:relative}
.abs{position:absolute}

/* header / hero */
.hero{left:0;top:0;width:1200px;height:660px;background:linear-gradient(180deg,#1c4d8a 0%,#2e78b2 35%,#3aa0c9 60%,#2d7a6a 80%,#5b8a4a 100%)}
.hero-wave{left:0;top:560px;width:1200px;height:110px}
.topbar{top:24px;right:34px;display:flex;align-items:center;gap:14px;color:var(--white);font:500 13px "Montserrat",sans-serif}
.topbar .mail{display:flex;align-items:center;gap:8px;margin-right:8px}
.social{width:26px;height:26px;border:1.5px solid var(--white);border-radius:6px;display:inline-block}
.logo{left:34px;top:62px;display:flex;align-items:center;gap:10px;color:var(--white);font:700 22px "Old Standard TT",serif;letter-spacing:.5px}
.logo .mark{width:20px;height:20px;border-radius:50%;background:var(--white)}
.nav{top:74px;left:0;width:1200px;height:20px;font:600 13px "Montserrat",sans-serif;color:var(--white)}
.nav span{position:absolute;top:0;white-space:nowrap}
.btn-nav{left:1058px;top:70px;width:112px;height:30px;border:1.5px solid var(--white);border-radius:6px;color:var(--white);font:700 13px "Montserrat",sans-serif;display:flex;align-items:center;justify-content:center}
.hero-title{top:242px;left:0;width:1200px;text-align:center;color:var(--white);font:700 47px "Old Standard TT",serif;letter-spacing:.5px}
.hero-sub{top:310px;left:0;width:1200px;text-align:center;color:var(--white);font:700 14px "Montserrat",sans-serif;letter-spacing:2px}
.hero-sub::before,.hero-sub::after{content:"";display:inline-block;width:18px;height:1px;background:var(--white);vertical-align:middle;margin:0 12px}
.btn-white{left:535px;top:358px;width:130px;height:34px;background:var(--white);border-radius:17px;color:var(--ink);font:600 12px "Montserrat",sans-serif;display:flex;align-items:center;justify-content:center}

/* booking bar */
.booking{left:90px;top:547px;width:1022px;height:121px;background:var(--white);border-radius:60px;box-shadow:0 10px 30px rgba(0,0,0,.12);overflow:hidden}
.booking .field{position:absolute;top:0;height:121px;width:170px}
.booking .label{position:absolute;top:30px;left:0;color:var(--lime);font:500 12px "Montserrat",sans-serif;white-space:nowrap}
.booking .value{position:absolute;top:52px;left:0;font:400 40px "Old Standard TT",serif;color:var(--ink);white-space:nowrap}
.booking .value small{font:400 13px "Open Sans",sans-serif;color:var(--muted)}
.booking .divider{position:absolute;top:30px;width:1px;height:60px;background:#e4e4e4}
.promo{position:absolute;left:806px;top:0;width:216px;height:121px;background:var(--grad)}
.promo .q{position:absolute;top:33px;left:0;width:216px;text-align:center;color:var(--white);font:500 12px "Montserrat",sans-serif}
.promo .btn{position:absolute;left:36px;top:57px;width:144px;height:34px;border-radius:17px;background:var(--white);color:var(--green);font:700 12px "Montserrat",sans-serif;display:flex;align-items:center;justify-content:center}

/* about */
.eyebrow{color:var(--lime);font:500 13px "Montserrat",sans-serif}
.section-title{color:var(--blue);font:700 46px "Old Standard TT",serif;line-height:1.25}
.about-title{left:90px;top:782px;width:520px}
.about-text{left:90px;top:930px;width:470px;font-size:14px;line-height:1.65;color:var(--muted)}
.about-text p+p{margin-top:14px}
.btn-grad{height:30px;border-radius:15px;background:var(--grad);color:var(--white);font:700 12px "Montserrat",sans-serif;display:flex;align-items:center;justify-content:center}
.photo{position:absolute}
.frame{position:absolute;background:var(--white);padding:12px;box-shadow:0 6px 18px rgba(0,0,0,.15)}
.frame div{width:100%;height:100%}

/* video band */
.video-band{left:0;top:1272px;width:1200px;height:435px;background:linear-gradient(120deg,#3b3a2a 0%,#6d5a40 35%,#8c7a5e 55%,#4d5a33 100%)}
.video-shade{left:0;top:1272px;width:1200px;height:435px;background:rgba(0,0,0,.28)}
.play{left:578px;top:1410px;width:44px;height:44px}
.video-title{left:0;top:1465px;width:1200px;text-align:center;color:var(--white);font:700 44px "Old Standard TT",serif;line-height:1.3}

/* properties */
.center{left:0;width:1200px;text-align:center}
.card{position:absolute;top:1905px;width:320px;height:405px;border:1px solid #e2e2e2;background:#f1f1f1}
.card.active{background:var(--white);border-color:transparent;box-shadow:0 10px 28px rgba(0,0,0,.12)}
.card .img{position:absolute;left:0;top:0;width:100%;height:250px;clip-path:path("M0 0 H320 V205 Q160 290 0 205 Z")}
.card .loc{position:absolute;top:270px;width:100%;text-align:center;color:var(--blue);font:400 13px "Montserrat",sans-serif;display:flex;justify-content:center;align-items:center;gap:6px}
.card .name{position:absolute;top:293px;width:100%;text-align:center;font:600 19px "Montserrat",sans-serif;color:var(--ink)}
.card .btn{position:absolute;left:104px;top:345px;width:112px;height:28px;border-radius:14px;font:700 12px "Montserrat",sans-serif;color:var(--white);display:flex;align-items:center;justify-content:center;background:var(--green)}
.card.active .btn{background:var(--grad)}
.arrow{position:absolute;width:16px;height:16px}

/* testimonials */
.avatar{left:562px;top:2502px;width:76px;height:76px;border-radius:50%;background:linear-gradient(160deg,#c9e6f2,#7fb7d0);border:3px solid var(--white);box-shadow:0 3px 10px rgba(0,0,0,.15)}
.quote{left:263px;top:2600px;width:674px;text-align:center;font-size:14px;line-height:1.6;color:var(--muted)}
.quote-name{top:2678px;font:600 15px "Montserrat",sans-serif;color:var(--ink)}
.quote-role{top:2701px;font-size:12px;color:var(--muted)}

/* footer */
.footer-bg{left:0;top:2860px;width:1200px;height:517px}
.tree-area{left:40px;top:2735px;width:140px;height:170px;background:linear-gradient(180deg,rgba(143,191,74,0) 0%,rgba(110,165,60,.55) 55%,rgba(88,125,51,.9) 100%)}
.f-head{top:3006px;color:var(--white);font:700 15px "Montserrat",sans-serif}
.f-text{color:var(--white);font-size:13px;line-height:1.6}
.f-call{left:88px;top:3062px;color:var(--white);font:700 19px "Montserrat",sans-serif}
.f-links{left:437px;top:3063px;list-style:none;color:var(--white);font-size:13px;line-height:27px}
.f-social{top:3218px;width:30px;height:30px;border:1.5px solid var(--white);border-radius:50%}
.map{left:617px;top:3008px;width:495px;height:243px;background:linear-gradient(135deg,#eceff1 0%,#dfe3e6 60%,#c9ced4 100%)}
.f-bottom{top:3305px;color:var(--white);font-size:12px}
</style>
</head>
<body>

<!-- hero -->
<div class="abs hero" role="img" aria-label="Photo of a turquoise Ibiza cove with pine-covered cliffs and anchored sailboats"></div>
<svg class="abs hero-wave" viewBox="0 0 1200 110" preserveAspectRatio="none" aria-hidden="true">
  <path d="M0 70 Q120 40 260 62 T520 55 T800 66 T1050 48 T1200 60 V110 H0 Z" fill="#f4f4f4"/>
</svg>

<div class="abs topbar">
  <span class="mail">
    <svg width="14" height="10" viewBox="0 0 14 10"><rect x=".5" y=".5" width="13" height="9" fill="none" stroke="#fff"/><path d="M.5 .5 L7 6 L13.5 .5" fill="none" stroke="#fff"/></svg>
    reservas@amberharbourvillas.example
  </span>
  <span class="social"></span>
  <span class="social" style="border-radius:50%"></span>
</div>

<div class="abs logo"><span class="mark"></span>AMBER HARBOUR</div>

<nav class="abs nav">
  <span style="left:330px">-- Home --</span>
  <span style="left:455px">About</span>
  <span style="left:545px">Properties</span>
  <span style="left:662px">Testimonials</span>
  <span style="left:795px">Contact</span>
  <span style="left:890px;display:flex;align-items:center;gap:8px">
    <svg width="13" height="13" viewBox="0 0 24 24"><path d="M6.6 10.8a15 15 0 0 0 6.6 6.6l2.2-2.2a1 1 0 0 1 1-.25 11.4 11.4 0 0 0 3.6.57 1 1 0 0 1 1 1V20a1 1 0 0 1-1 1A17 17 0 0 1 3 4a1 1 0 0 1 1-1h3.5a1 1 0 0 1 1 1c0 1.25.2 2.45.57 3.57a1 1 0 0 1-.25 1z" fill="#fff"/></svg>
    +34600418275
  </span>
</nav>
<div class="abs btn-nav">Book Now!</div>

<h1 class="abs hero-title">Enjoy a Luxury Experience</h1>
<div class="abs hero-sub">ENJOY WITH US</div>
<div class="abs btn-white">Contact Us</div>

<!-- booking -->
<div class="abs booking">
  <div class="field" style="left:52px">
    <span class="label">Check - In</span>
    <span class="value">02 <small>/ May</small></span>
    <svg class="abs" style="left:133px;top:75px" width="12" height="8" viewBox="0 0 12 8"><path d="M1 1l5 5 5-5" stroke="#666" stroke-width="1.5" fill="none"/></svg>
  </div>
  <div class="divider" style="left:225px"></div>
  <div class="field" style="left:268px">
    <span class="label">Check - Out</span>
    <span class="value">04 <small>/ May</small></span>
    <svg class="abs" style="left:133px;top:75px" width="12" height="8" viewBox="0 0 12 8"><path d="M1 1l5 5 5-5" stroke="#666" stroke-width="1.5" fill="none"/></svg>
  </div>
  <div class="divider" style="left:441px"></div>
  <div class="field" style="left:484px">
    <span class="label">Adults</span>
    <span class="value">02</span>
    <svg class="abs" style="left:94px;top:58px" width="10" height="20" viewBox="0 0 10 20"><path d="M1 6l4-4 4 4M1 14l4 4 4-4" stroke="#666" stroke-width="1.3" fill="none"/></svg>
  </div>
  <div class="divider" style="left:626px"></div>
  <div class="field" style="left:664px">
    <span class="label">Children</span>
    <span class="value">01</span>
    <svg class="abs" style="left:95px;top:58px" width="10" height="20" viewBox="0 0 10 20"><path d="M1 6l4-4 4 4M1 14l4 4 4-4" stroke="#666" stroke-width="1.3" fill="none"/></svg>
  </div>
  <div class="promo">
    <div class="q">Have a Promo Code?</div>
    <div class="btn">Book Now!</div>
  </div>
</div>

<!-- about -->
<div class="abs eyebrow center" style="top:743px">Little About Us</div>
<h2 class="abs section-title about-title">A best place to enjoy<br>your life</h2>
<div class="abs about-text">
  <p>Amber Harbour Villas is a company specialized in offering its clients accommodation in Villas on the countryside of Ibiza. Our guests enjoy the rural Ibiza, tranquility, relax, private pool, close to dream beaches and coves, the best restaurants, an unforgettable holiday for family or friends.</p>
  <p>Every day can be a different experience, beach, restaurant, flea market, disco, hiking, kayaking, horseback riding, shopping, history, boat ride! There is a lot of variety for all budgets ...</p>
</div>
<div class="abs btn-grad" style="left:90px;top:1159px;width:126px">Contact Us</div>

<div class="photo" style="left:680px;top:810px;width:432px;height:176px;background:linear-gradient(160deg,#3c7a3a 0%,#2aa1c6 45%,#1b7fb4 75%,#6c9a44 100%)" role="img" aria-label="Photo of a rocky Ibiza cove with clear turquoise water and pines"></div>
<div class="frame" style="left:617px;top:930px;width:295px;height:196px"><div style="background:linear-gradient(180deg,#2a8fc6 0%,#3f9a5a 55%,#2f7a2c 100%)" role="img" aria-label="Underwater photo of green posidonia seagrass meadow"></div></div>
<div class="frame" style="left:795px;top:1013px;width:191px;height:173px"><div style="background:linear-gradient(180deg,#4fb4dc 0%,#3f9d6a 55%,#2e7d2e 100%)" role="img" aria-label="Underwater photo of posidonia seagrass lit by sunlight"></div></div>

<!-- video -->
<div class="abs video-band" role="img" aria-label="Video still of a villa terrace with palm trees and outdoor dining"></div>
<div class="abs video-shade"></div>
<svg class="abs play" viewBox="0 0 44 44" aria-label="Play video">
  <circle cx="22" cy="22" r="20" fill="none" stroke="#fff" stroke-width="2.5"/>
  <path d="M17 13 L31 22 L17 31 Z" fill="#fff"/>
</svg>
<h2 class="abs video-title">The best way to stay in<br>Ibiza!</h2>

<!-- properties -->
<div class="abs eyebrow center" style="top:1783px">Book Your Stay</div>
<h2 class="abs section-title center" style="top:1810px">Enjoy a Luxury Experience</h2>

<svg class="arrow" style="left:36px;top:2099px" viewBox="0 0 16 16"><path d="M11 2L5 8l6 6" stroke="#333" stroke-width="2" fill="none"/></svg>
<svg class="arrow" style="left:1148px;top:2099px" viewBox="0 0 16 16"><path d="M5 2l6 6-6 6" stroke="#333" stroke-width="2" fill="none"/></svg>

<div class="card" style="left:88px">
  <div class="img" style="background:linear-gradient(180deg,#4a8fd0 0%,#6f9a58 45%,#1e9ad6 100%)" role="img" aria-label="Photo of a villa pool with sun loungers and palms"></div>
  <div class="loc"><svg width="10" height="14" viewBox="0 0 10 14"><path d="M5 13S1 8 1 5a4 4 0 0 1 8 0c0 3-4 8-4 8z" fill="none" stroke="#2b9ad3" stroke-width="1.3"/><circle cx="5" cy="5" r="1.4" fill="#2b9ad3"/></svg>Saint Joseph</div>
  <div class="name">Villa Can Rovira</div>
  <div class="btn">View Detail</div>
</div>
<div class="card active" style="left:439px">
  <div class="img" style="background:linear-gradient(180deg,#2f6fc0 0%,#d6d2c6 40%,#4c7a36 100%)" role="img" aria-label="Photo of a white Ibiza villa among trees"></div>
  <div class="loc"><svg width="10" height="14" viewBox="0 0 10 14"><path d="M5 13S1 8 1 5a4 4 0 0 1 8 0c0 3-4 8-4 8z" fill="none" stroke="#2b9ad3" stroke-width="1.3"/><circle cx="5" cy="5" r="1.4" fill="#2b9ad3"/></svg>Santa Eulalia</div>
  <div class="name">Villa Can Pastor</div>
  <div class="btn">View Detail</div>
</div>
<div class="card" style="left:792px">
  <div class="img" style="background:linear-gradient(180deg,#3d86cf 0%,#c98f74 40%,#2aa3dc 100%)" role="img" aria-label="Photo of a villa with red roofs beside a large pool"></div>
  <div class="loc"><svg width="10" height="14" viewBox="0 0 10 14"><path d="M5 13S1 8 1 5a4 4 0 0 1 8 0c0 3-4 8-4 8z" fill="none" stroke="#2b9ad3" stroke-width="1.3"/><circle cx="5" cy="5" r="1.4" fill="#2b9ad3"/></svg>Saint Joseph</div>
  <div class="name">Villa Can Rovira</div>
  <div class="btn">View Detail</div>
</div>

<!-- testimonials -->
<div class="abs eyebrow center" style="top:2386px">Testimonials</div>
<h2 class="abs section-title center" style="top:2413px">Our Guests Say</h2>
<svg class="arrow" style="left:510px;top:2532px;width:12px;height:12px" viewBox="0 0 16 16"><path d="M11 2L5 8l6 6" stroke="#555" stroke-width="2" fill="none"/></svg>
<svg class="arrow" style="left:678px;top:2532px;width:12px;height:12px" viewBox="0 0 16 16"><path d="M5 2l6 6-6 6" stroke="#555" stroke-width="2" fill="none"/></svg>
<div class="abs avatar" role="img" aria-label="Guest portrait photo"></div>
<p class="abs quote">There are many variations of passages of Lorem Ipsum available, but the majority have suffered alteration in some form, by injected humour, or randomised words which don't look even slightly believable. If you are going to use a passage of Lorem Ipsum ...</p>
<div class="abs center quote-name">Standard Chunk</div>
<div class="abs center quote-role">Lorem Ipsum</div>
<div class="abs btn-grad" style="left:544px;top:2737px;width:112px;height:28px;background:var(--green)">View All</div>

<!-- footer -->
<svg class="abs footer-bg" viewBox="0 0 1200 517" preserveAspectRatio="none" aria-hidden="true">
  <defs><linearGradient id="footerGrad" x1="0" x2="1" y1="0" y2="0"><stop offset="0" stop-color="#587d33"/><stop offset=".5" stop-color="#3f9a8a"/><stop offset="1" stop-color="#2fa7dc"/></linearGradient></defs>
  <path d="M0 40 Q150 10 320 34 T640 28 T930 50 T1200 22 V517 H0 Z" fill="url(#footerGrad)"/>
</svg>
<div class="abs tree-area" role="img" aria-label="Illustration of a pine tree at the edge of the footer"></div>

<div class="abs f-head" style="left:88px">Contact Us</div>
<div class="abs f-call">Call: +34600418275</div>
<div class="abs f-text" style="left:88px;top:3091px">reservas@amberharbourvillas.example</div>
<div class="abs f-text" style="left:88px;top:3130px;width:250px">Carrer de les Salines, 8, Santa Eularia Des Riu, 07840, Ibiza, Spain</div>
<span class="abs f-social" style="left:88px"></span>
<span class="abs f-social" style="left:128px"></span>

<div class="abs f-head" style="left:437px">Quick Links</div>
<ul class="abs f-links">
  <li>Home</li><li>About</li><li>Properties</li><li>Testimonials</li><li>Contact</li>
</ul>

<div class="abs map" role="img" aria-label="Street map showing the office location in Santa Eularia"></div>

<div class="abs f-bottom" style="left:88px">© 2019 <b>Amber Harbour Villas</b>. All Rights Reserved</div>
<div class="abs f-bottom" style="left:617px">Privacy Policy &nbsp;&nbsp;|&nbsp;&nbsp; Terms &amp; Conditions</div>

</body>
</html>
```